Calder Ridge Minerals

Looking for a cool, glossy business card...white with our logo on one side and then the a smaller version of the logo on the other side (top left hand corner) and then the name and position of the person next to it, and then the office address and email address on the bottom left hand corner and the phone numbers & email address on the bottom right hand corner. I have the logo already...can pass it on when you're ready.

```html
<!DOCTYPE html>
<html lang="en">
<head>
<meta charset="utf-8">
<title>Calder Ridge Minerals – Business Card</title>
<link href="https://fonts.googleapis.com/css2?family=Cinzel:wght@400;600&family=Montserrat:wght@300;400&display=swap" rel="stylesheet">
<style>
  :root {
    --backdrop: #e6e7ea;
    --card: #ffffff;
    --ink: #2f2f33;
    --ink-soft: #4a4a50;
    --blue: #2b3f9e;
    --red: #d21f2b;
    --mist: #f1f2f4;
  }
  * { box-sizing: border-box; margin: 0; padding: 0; }
  html, body {
    width: 1200px; height: 965px; overflow: hidden;
    background: var(--backdrop);
  }
  .sheet {
    width: 1200px; height: 965px;
    display: flex; flex-direction: column; align-items: center; justify-content: center;
    gap: 40px;
  }
  .card {
    position: relative;
    width: 700px; height: 400px;
    background: var(--card);
    box-shadow: 0 6px 18px rgba(0,0,0,0.12);
  }
  /* Front */
  .card--front {
    display: flex; align-items: center; justify-content: center;
    background: radial-gradient(ellipse at 30% 60%, var(--mist) 0%, var(--card) 55%);
  }
  .wordmark {
    display: flex; align-items: center; gap: 14px;
  }
  .wordmark__square {
    width: 18px; height: 18px; background: var(--blue);
  }
  .wordmark__name {
    font-family: "Cinzel", serif;
    font-weight: 400;
    color: var(--ink);
    letter-spacing: 1px;
    white-space: nowrap;
  }
  .card--front .wordmark__name { font-size: 44px; }
  /* Back */
  .card--back .wordmark {
    position: absolute; left: 48px; top: 48px;
  }
  .card--back .wordmark__square { width: 12px; height: 12px; }
  .card--back .wordmark__name { font-size: 26px; }
  .person {
    position: absolute; left: 48px; top: 200px;
  }
  .person__name {
    font-family: "Cinzel", serif; font-weight: 600;
    font-size: 34px; color: var(--blue); letter-spacing: 1px;
  }
  .person__role {
    font-family: "Montserrat", sans-serif; font-weight: 300;
    font-size: 20px; color: var(--ink-soft); margin-top: 2px;
  }
  .contact {
    position: absolute; bottom: 40px;
    font-family: "Montserrat", sans-serif; font-weight: 300;
    font-size: 17px; color: var(--ink); line-height: 1.55;
    list-style: none;
  }
  .contact--office { left: 48px; }
  .contact--direct { right: 44px; text-align: right; }
  .contact li { display: flex; align-items: center; gap: 10px; }
  .contact--direct li { justify-content: flex-end; }
  .icon { width: 15px; height: 15px; fill: var(--red); flex: none; }
</style>
</head>
<body>
<main class="sheet">
  <section class="card card--front" aria-label="Card front">
    <div class="wordmark">
      <span class="wordmark__square"></span>
      <span class="wordmark__name">Calder Ridge Minerals</span>
    </div>
  </section>

  <section class="card card--back" aria-label="Card back">
    <div class="wordmark">
      <span class="wordmark__square"></span>
      <span class="wordmark__name">Calder Ridge Minerals</span>
    </div>

    <div class="person">
      <h1 class="person__name">DALE WHITCOMB</h1>
      <p class="person__role">General Manager</p>
    </div>

    <ul class="contact contact--office">
      <li>
        <svg class="icon" viewBox="0 0 24 24" aria-hidden="true"><path d="M12 2a7 7 0 0 0-7 7c0 5 7 13 7 13s7-8 7-13a7 7 0 0 0-7-7zm0 9.5a2.5 2.5 0 1 1 0-5 2.5 2.5 0 0 1 0 5z"/></svg>
        1/3 first address, State. City ZIP
      </li>
      <li>
        <svg class="icon" viewBox="0 0 24 24" aria-hidden="true"><path d="M2 5h20v14H2z" fill="none"/><path d="M2 5h20l-10 8z"/><path d="M2 7l10 8 10-8v12H2z"/></svg>
        info@calderridgeminerals.com
      </li>
    </ul>

    <ul class="contact contact--direct">
      <li>+00 000 00 00 00
        <svg class="icon" viewBox="0 0 24 24" aria-hidden="true"><path d="M6.6 10.8a15 15 0 0 0 6.6 6.6l2.2-2.2a1 1 0 0 1 1-.25 11.4 11.4 0 0 0 3.6.57 1 1 0 0 1 1 1V20a1 1 0 0 1-1 1A17 17 0 0 1 3 4a1 1 0 0 1 1-1h3.5a1 1 0 0 1 1 1c0 1.25.2 2.45.57 3.6a1 1 0 0 1-.25 1z"/></svg>
      </li>
      <li>+00 000 00 00 00
        <svg class="icon" viewBox="0 0 24 24" aria-hidden="true"><path d="M6.6 10.8a15 15 0 0 0 6.6 6.6l2.2-2.2a1 1 0 0 1 1-.25 11.4 11.4 0 0 0 3.6.57 1 1 0 0 1 1 1V20a1 1 0 0 1-1 1A17 17 0 0 1 3 4a1 1 0 0 1 1-1h3.5a1 1 0 0 1 1 1c0 1.25.2 2.45.57 3.6a1 1 0 0 1-.25 1z"/></svg>
      </li>
      <li>info@dalewhitcomb.com
        <svg class="icon" viewBox="0 0 24 24" aria-hidden="true"><path d="M2 5h20l-10 8z"/><path d="M2 7l10 8 10-8v12H2z"/></svg>
      </li>
    </ul>
  </section>
</main>
</body>
</html>
```